Postcard Design

Need postcard design for dental office. The doctor is returning to the office after a few months medical leave and he wants a postcard to be mailed to patients and families in the surrounding area to create new patients. We have attached a rough sketch of the information we would like to include on the postcard along with color selection but are open to additional artwork or design to improve the overall look. We are also including a photo of the dentist for the front of the postcard. We plan to have the metered postage through Plentomark if possible so please let me know how that works because I'm assuming that will need to be included in the design. I am also attaching a sample of a postcard that the dentist received in the mail from a Corbridge doctor and would like his postcard to resemble this layout. The postcard needs to 8.5 x 5.5; I believe this is called the oversized selection for Plentomark and we are planning to have them do the printing. Please verify you did receive four attached files including photo, front sketch, back sketch, and actual postcard example.

Thank you,
Marlene Tofsky

```html
<!DOCTYPE html>
<html lang="en">
<head>
<meta charset="utf-8">
<title>General Dentist Postcard</title>
<link href="https://fonts.googleapis.com/css2?family=Open+Sans:ital,wdth,wght@0,75,400..800;1,75,400..800&display=swap" rel="stylesheet">
<style>
  :root {
    --navy: #16425f;
    --sky: #2f9fdd;
    --teal: #2f9ea3;
    --teal-light: #d9ecef;
    --ink: #26323a;
    --paper: #ffffff;
    --canvas: #e9e6e1;
    --rule: #b9bcbf;
  }
  * { margin: 0; padding: 0; box-sizing: border-box; }
  html, body { width: 1200px; height: 500px; overflow: hidden; }
  body {
    background: var(--canvas);
    font-family: "Open Sans", "Arial Narrow", sans-serif;
    font-stretch: 75%;
    color: var(--ink);
    position: relative;
  }
  p, address, span, div { white-space: nowrap; }
  .card {
    position: absolute;
    top: 32px;
    width: 560px;
    height: 433px;
    background: var(--paper);
    overflow: hidden;
  }
  .card--front { left: 28px; }
  .card--back { left: 612px; }

  /* Front */
  .front-art { position: absolute; left: 0; top: 0; width: 560px; height: 338px; }
  .portrait {
    position: absolute; left: 0; top: 0; width: 250px; height: 338px;
    background: linear-gradient(180deg, #9fc3cf 0%, #6d8796 40%, #2b3641 70%, #1b232c 100%);
    clip-path: path("M0 0 H268 C233 70 219 160 225 250 C227 290 233 318 237 338 H0 Z");
  }
  .brand { position: absolute; text-align: center; color: var(--navy); line-height: 1; }
  .brand__top { font-weight: 400; letter-spacing: 5px; }
  .brand__bottom { font-weight: 800; letter-spacing: 4px; }
  .card--front .brand { left: 365px; top: 28px; width: 170px; }
  .card--front .brand__top { font-size: 28px; }
  .card--front .brand__bottom { font-size: 31px; margin-top: 1px; }
  .brand__underline { display: block; width: 112px; height: 4px; background: var(--teal); margin: 5px auto 0; }
  .front-tagline {
    position: absolute; left: 250px; top: 110px; width: 285px;
    text-align: center; font-style: italic; font-size: 23px; line-height: 29px; color: var(--navy);
  }
  .front-doctor {
    position: absolute; left: 245px; top: 186px; width: 300px;
    text-align: center; font-weight: 700; font-size: 24px; color: var(--sky);
  }
  .phone { display: inline-flex; align-items: center; gap: 4px; font-weight: 700; letter-spacing: 1px; }
  .phone svg { flex: none; }
  .front-phone { position: absolute; left: 250px; top: 224px; width: 290px; text-align: center; font-size: 22px; color: var(--navy); }
  .front-address {
    position: absolute; left: 260px; top: 270px; width: 270px; font-style: normal;
    text-align: center; font-weight: 700; font-size: 13.5px; line-height: 17px; color: var(--ink);
  }
  .front-band {
    position: absolute; top: 338px; height: 80px; background: var(--navy); color: var(--paper);
  }
  .front-band--left { left: 0; width: 277px; display: flex; align-items: center; justify-content: center; }
  .front-band--left span { color: var(--sky); font-size: 25px; font-weight: 500; }
  .front-band--right { left: 281px; width: 279px; text-align: center; padding-top: 6px; }
  .front-band__lead { font-size: 17px; font-weight: 600; line-height: 22px; }
  .front-band__phone { font-size: 23px; line-height: 26px; }
  .front-band__web { font-size: 19px; font-weight: 700; color: var(--sky); line-height: 24px; letter-spacing: 0.5px; }

  /* Back */
  .back-header {
    position: absolute; left: 0; top: 0; width: 560px; height: 96px; background: var(--navy); color: var(--paper);
  }
  .back-stripe { position: absolute; left: 0; top: 96px; width: 560px; height: 12px; background: var(--sky); }
  .card--back .brand { left: 20px; top: 30px; width: 150px; color: var(--paper); }
  .card--back .brand__top { font-size: 23px; }
  .card--back .brand__bottom { font-size: 27px; margin-top: 2px; }
  .back-contact { position: absolute; left: 185px; top: 18px; width: 365px; text-align: center; line-height: 23px; }
  .back-contact__title { font-size: 21px; font-weight: 700; }
  .back-contact__call { font-size: 20px; letter-spacing: 1.5px; }
  .back-contact__web { font-size: 20px; }
  .back-contact__web strong { font-weight: 700; }
  .bio-panel {
    position: absolute; left: 0; top: 108px; width: 270px; height: 325px;
    background: linear-gradient(90deg, var(--teal-light) 0%, #9fd0d4 55%, var(--teal) 100%);
    padding: 26px 10px 0 9px; font-size: 15px; line-height: 19px; color: var(--ink);
  }
  .bio-panel p + p { margin-top: 9px; }
  .stamp-box { position: absolute; left: 458px; top: 123px; width: 82px; height: 75px; border: 1px solid var(--rule); }
  .address-lines { position: absolute; left: 323px; top: 266px; width: 217px; }
  .address-lines span { display: block; height: 1px; background: var(--rule); margin-bottom: 31px; }
</style>
</head>
<body>

<section class="card card--front" aria-label="Postcard front">
  <svg class="front-art" viewBox="0 0 560 338" aria-hidden="true">
    <defs>
      <linearGradient id="front-wash" x1="0" y1="0" x2="1" y2="0">
        <stop offset="0" stop-color="#7fb8cc"/>
        <stop offset="1" stop-color="#e3f1f5"/>
      </linearGradient>
    </defs>
    <path d="M0 0 H272 C236 70 222 160 228 250 C230 290 236 318 240 338 H0 Z" fill="url(#front-wash)"/>
    <path d="M272 0 C236 70 222 160 228 250 C230 290 236 318 240 338" fill="none" stroke="var(--sky)" stroke-width="5"/>
  </svg>
  <div class="portrait" role="img" aria-label="Portrait photograph of the dentist in a dark suit and tie"></div>

  <div class="brand">
    <div class="brand__top">GENERAL</div>
    <div class="brand__bottom">DENTIST</div>
    <span class="brand__underline"></span>
  </div>
  <p class="front-tagline">Now Accepting Established<br>and New Patients</p>
  <p class="front-doctor">Dr. Len T. Harrow, DDS, FAGD</p>
  <p class="front-phone"><span class="phone">
    <svg width="18" height="18" viewBox="0 0 18 18"><circle cx="9" cy="9" r="8" fill="none" stroke="currentColor" stroke-width="2"/><path d="M6 4 C4 8 5 12 9 14 L10 12 C8 11 7 9 8 7 Z" fill="currentColor"/></svg>
    770.555.0148</span></p>
  <address class="front-address">
    Lindale Park<br>4820-B Maple Crest Blvd, Suite A<br>Lindale Park, GA 30199
  </address>
  <div class="front-band front-band--left"><span>NOW ACCEPTING PATIENTS</span></div>
  <div class="front-band front-band--right">
    <p class="front-band__lead">For More Information, Please Call</p>
    <p class="front-band__phone"><span class="phone">
      <svg width="18" height="18" viewBox="0 0 18 18"><circle cx="9" cy="9" r="8" fill="none" stroke="currentColor" stroke-width="2"/><path d="M6 4 C4 8 5 12 9 14 L10 12 C8 11 7 9 8 7 Z" fill="currentColor"/></svg>
      770.555.0148</span></p>
    <p class="front-band__web">www.DrLenHarrow.com</p>
  </div>
</section>

<section class="card card--back" aria-label="Postcard back">
  <header class="back-header">
    <div class="brand">
      <div class="brand__top">GENERAL</div>
      <div class="brand__bottom">DENTIST</div>
    </div>
    <div class="back-contact">
      <p class="back-contact__title">Accepting Established and New Patients</p>
      <p class="back-contact__call">Call <span class="phone">
        <svg width="16" height="16" viewBox="0 0 18 18"><circle cx="9" cy="9" r="8" fill="none" stroke="currentColor" stroke-width="2"/><path d="M6 4 C4 8 5 12 9 14 L10 12 C8 11 7 9 8 7 Z" fill="currentColor"/></svg>
        770.555.0148</span></p>
      <p class="back-contact__web">Or visit us at<strong>: www.DrLenHarrow.com</strong></p>
    </div>
  </header>
  <div class="back-stripe"></div>
  <div class="bio-panel">
    <p>Len T. Harrow DDS, FAGD, a native of<br>Lindale Park, GA earned his Doctorate<br>of Dental Surgery at Ashcombe<br>University Dental School in Fairmont.</p>
    <p>Dr. Harrow has been improving the<br>dental health of patients in Western<br>Georgia for over 25 years.</p>
  </div>
  <div class="stamp-box"></div>
  <div class="address-lines"><span></span><span></span><span></span><span></span></div>
</section>

</body>
</html>
```